Perfume packaging design

We are a company producing perfumery and deodorants in the upper mass market segment (semi-selective). We need a packaging design for our new fragrance for women called Moon Petal. You will find attached a picture of the chosen bottle and cap along with specification.

The fragrance is modern and delicate. It is sweet with floral accent and notes of mandarin, rose, peach.

Suitable for evening perfume as well as casual daily.

Looking for:
1. logo - "Moon Petal" on bottle and packaging
2. Color of the perfume
3. Design of the carton box

Product is 100ml eau de perfume for women.

Target Market(s)

Target market is Eastern Europe and middle east

Women
Age 30-45
Price range - semi-selective
Sales channels - perfumeries, drug stores and online

Industry/Entity Type

It Company

Requirements
Must have
• Packaging - carton
Perfume should be colored
Embosing
Nice to have
• Golden hot stamping or other golden element

```html
<!DOCTYPE html>
<html lang="en">
<head>
<meta charset="utf-8">
<title>Moon Petal – Carton Dieline</title>
<link href="https://fonts.googleapis.com/css2?family=Cinzel:wght@600&family=Great+Vibes&family=Montserrat:wght@400;500&display=swap" rel="stylesheet">
<style>
  :root {
    --paper: #ffffff;
    --die: #e6007e;
    --gold: #b89b5e;
    --gold-light: #d2b87a;
    --ink: #0b0b0d;
    --violet-deep: #3a3550;
    --violet-mid: #7c7698;
    --violet-pale: #c9c5dc;
    --lace-dark: #1a1424;
    --lace-light: #5e4a86;
    --rule: #7a7a7a;
  }
  * { margin: 0; padding: 0; box-sizing: border-box; }
  html, body { width: 1200px; height: 1000px; overflow: hidden; background: var(--paper); }
  .sheet { position: relative; width: 1200px; height: 1000px; font-family: "Montserrat", sans-serif; }

  .panel { position: absolute; }
  .lid-panel {
    left: 578px; top: 117px; width: 234px; height: 231px;
    background: radial-gradient(ellipse at 60% 45%, var(--violet-pale) 0%, var(--violet-mid) 60%, var(--violet-deep) 100%);
  }
  .wrap-band {
    left: 126px; top: 348px; width: 919px; height: 242px;
    background: linear-gradient(180deg, var(--violet-deep) 0%, var(--violet-mid) 25%, var(--violet-pale) 45%, #8a7fb0 70%, #5a4c80 100%);
  }
  .lace-border {
    left: 126px; top: 510px; width: 919px; height: 80px;
    background: linear-gradient(180deg, rgba(26,20,36,0) 0%, var(--lace-light) 15%, var(--lace-dark) 55%, #2a2038 100%);
  }
  .base-panel { left: 585px; top: 590px; width: 227px; height: 222px; background: var(--ink); }

  .label {
    position: absolute; background: var(--ink); border-radius: 22px;
    display: flex; flex-direction: column; align-items: center; justify-content: center;
    color: var(--gold); text-align: center;
  }
  .label--main { width: 156px; height: 78px; }
  .label--small { width: 124px; height: 64px; }
  .label__brand { font-family: "Cinzel", serif; font-weight: 600; font-size: 20px; letter-spacing: 1px; line-height: 1; color: var(--gold-light); }
  .label--small .label__brand { font-size: 15px; }
  .front-copy { position: absolute; width: 200px; text-align: center; color: var(--gold); }
  .front-copy__type { font-family: "Great Vibes", cursive; font-size: 20px; line-height: 1; color: var(--gold-light); }
  .front-copy__spray { font-size: 6.5px; letter-spacing: .6px; margin-top: 10px; font-weight: 500; }
  .volume { position: absolute; font-size: 7px; color: var(--gold); }

  .legend { position: absolute; left: 170px; display: flex; align-items: center; gap: 8px; font-size: 9px; }
  .legend__swatch { width: 20px; height: 20px; }
  .legend--gold { top: 771px; color: var(--gold); }
  .legend--gold .legend__swatch { background: var(--gold); }
  .legend--die { top: 804px; color: var(--die); }
  .legend--die .legend__swatch { background: var(--die); }

  .overlay { position: absolute; left: 0; top: 0; }
  .dim-text { font-family: "Montserrat", sans-serif; font-size: 7px; fill: #555; }
</style>
</head>
<body>
<main class="sheet">
  <div class="panel lid-panel" role="img" aria-label="Soft violet night sky with pale white blossoms and sparkles"></div>
  <div class="panel wrap-band" role="img" aria-label="Violet misty background with pale white flowers and stars"></div>
  <div class="panel lace-border" role="img" aria-label="Black floral lace border"></div>
  <div class="panel base-panel"></div>

  <div class="label label--small" style="left:633px; top:205px;"><span class="label__brand">Moon Petal</span></div>

  <div class="label label--main" style="left:165px; top:398px;"><span class="label__brand">Moon Petal</span></div>
  <div class="front-copy" style="left:143px; top:446px;">
    <div class="front-copy__type">Eau De Parfume</div>
    <div class="front-copy__spray">VAPORISATEUR - NATURAL SPAY</div>
  </div>

  <div class="label label--small" style="left:410px; top:404px;"><span class="label__brand">Moon Petal</span></div>

  <div class="label label--main" style="left:620px; top:398px;"><span class="label__brand">Moon Petal</span></div>
  <div class="front-copy" style="left:598px; top:446px;">
    <div class="front-copy__type">Eau De Parfume</div>
    <div class="front-copy__spray">VAPORISATEUR - NATURAL SPAY</div>
  </div>
  <span class="volume" style="left:598px; top:561px;">100ml ℮</span>
  <span class="volume" style="left:768px; top:561px;">1.6 fl.oz</span>

  <div class="label label--small" style="left:866px; top:404px;"><span class="label__brand">Moon Petal</span></div>

  <div class="legend legend--gold"><span class="legend__swatch"></span>PANTONE 872 C = GOLDEN HOT STAMPING</div>
  <div class="legend legend--die"><span class="legend__swatch"></span>PANTONE MAGENTA C = DIE CUT</div>

  <svg class="overlay" width="1200" height="1000" viewBox="0 0 1200 1000" aria-hidden="true">
    <g fill="none" stroke="var(--die)" stroke-width="1">
      <path d="M126,350 L87,368 L87,572 L126,590"/>
      <path d="M585,117 L585,97 Q587,72 612,72 L786,72 Q810,72 812,97 L812,117"/>
      <path d="M585,812 L585,838 Q587,862 612,862 L786,862 Q810,862 812,838 L812,812"/>
      <path d="M360,348 L360,312 L388,255 L585,255"/>
      <path d="M812,255 L1008,255 L1030,332 L1045,348"/>
      <path d="M360,590 L360,628 L388,683 L585,683"/>
      <path d="M812,683 L1008,683 L1030,610 L1045,590"/>
      <path d="M126,348 L578,348 M812,348 L1045,348 L1045,590 L812,590 M585,590 L126,590 L126,348"/>
      <path d="M578,117 L812,117 L812,348 M578,117 L578,348"/>
      <path d="M585,590 L585,812 L812,812 L812,590"/>
      <g stroke-dasharray="3 3">
        <path d="M358,348 V590 M585,348 V590 M812,348 V590"/>
        <path d="M585,348 H812 M585,590 H812"/>
        <path d="M585,127 H805 M585,804 H805"/>
      </g>
    </g>

    <g stroke="var(--rule)" stroke-width=".6" fill="none">
      <path d="M1080,72 V862"/>
      <path d="M1070,72 H1090 M1070,117 H1090 M1070,255 H1090 M1070,355 H1090 M1070,580 H1090 M1070,683 H1090 M1070,808 H1090 M1070,862 H1090"/>
      <path d="M87,893 H1037 M87,887 V920 M1037,887 V920"/>
      <path d="M87,915 H1037 M132,910 V920 M358,910 V920 M584,910 V920 M810,910 V920"/>
      <path d="M0,48 H40 M60,0 V40 M1160,48 H1200 M1140,0 V40 M0,952 H40 M60,960 V1000 M1160,952 H1200 M1140,960 V1000"/>
    </g>
    <g class="dim-text" text-anchor="middle">
      <text transform="translate(1104,100) rotate(-90)">21 mm</text>
      <text transform="translate(1104,230) rotate(-90)">90 mm</text>
      <text transform="translate(1070,305) rotate(-90)">40 mm</text>
      <text transform="translate(1104,465) rotate(-90)">90 mm</text>
      <text transform="translate(1086,465) rotate(-90)">314 mm</text>
      <text transform="translate(1070,635) rotate(-90)">40 mm</text>
      <text transform="translate(1104,745) rotate(-90)">90 mm</text>
      <text transform="translate(1104,835) rotate(-90)">21 mm</text>
      <text x="570" y="890">378 mm</text>
      <text x="108" y="918">18 mm</text>
      <text x="245" y="918">90 mm</text>
      <text x="471" y="918">90 mm</text>
      <text x="697" y="918">90 mm</text>
      <text x="923" y="918">90 mm</text>
    </g>
  </svg>
</main>
</body>
</html>
```